QM - menu design

Hi,

We require elegant menu design for upscale restaurant. Please find attached the logo and the menu items for your reference.

for inspiration, this is a good website: -
http://www.plivermark.com/tablefolio/about.php

We are very much open for Menu Size suggestions.

unfortunately the place is going under renovation, we don't have updated images to it. the closest look and feel to our place is http://vessora.com ..

we are also open for creative options on the shape, the styles, etc. as long as it represents the fine dine feel ...

Thanks ...
Updates

Dear All,

We wouldlike to extend our apology for not being able to provide feedbacks on everysingle design. We were extremely busy and we have multiple contests opensimultaneously which makes the process even harder.

However,we would like to thank you all for the efforts you have put into designingour menu. It is very much appreciated …

We wishyou all success in your design ventures and we are quite positive that we willbe working with many of you on many projects in the soon future. 

Thanks & Regards,

DHI Team...

 

 

 

Industry/Entity Type

Restaurant

Requirements
Must have
• Please ensure that there are 'some' images in the menu ... this is very important.
Should not have
• IMPORTANT: -

1. Please DO NOT insert any currency sign to the menu
2. Please keep the prices of the menu at the end of the menu items descriptions NOT beside the menu item names. The font of the price should be similar to the menu item description and please DO NOT bold the numbers. the prices should be subtle.

Thank you ...

```html
<!DOCTYPE html>
<html lang="en">
<head>
<meta charset="utf-8">
<title>Quay Meridian Café – Menu</title>
<link href="https://fonts.googleapis.com/css2?family=Jost:wght@400&display=swap" rel="stylesheet">
<style>
  :root {
    --page: #ffffff;
    --card: #ffffff;
    --card-edge: #cfcfcf;
    --bronze: #a88769;
    --bronze-light: #c7ae96;
    --ink: #231f20;
    --body-text: #4a4a4a;
    --sand: #e2d9cf;
    --stone: #c9c6c3;
    --menu-text: #f3ece4;
  }
  * { margin: 0; padding: 0; box-sizing: border-box; }
  html, body { width: 1200px; height: 1191px; overflow: hidden; background: var(--page); }
  body { position: relative; font-family: "Jost", "Futura", sans-serif; font-weight: 400; }
  h1, h2, p { font-weight: 400; }

  .card {
    position: absolute;
    width: 441px;
    height: 880px;
    background: var(--card);
    border: 1px solid var(--card-edge);
    box-shadow: 2px 3px 5px rgba(0,0,0,0.18);
  }
  .card--cover { left: 128px; top: 102px; }
  .card--breakfast { left: 626px; top: 170px; }

  .cover-art { position: absolute; left: 0; top: 0; width: 441px; height: 880px; }
  .side-art { position: absolute; left: 362px; top: 29px; width: 45px; height: 820px; }

  .brand { position: absolute; color: var(--ink); line-height: 1.15; }
  .brand--cover { left: 30px; top: 92px; font-size: 24px; letter-spacing: 4px; }
  .brand--cover .brand-sub { display: block; }
  .brand--small { left: 24px; top: 812px; font-size: 10px; letter-spacing: 2px; }

  .menu-label {
    position: absolute; left: 246px; top: 675px; width: 161px; height: 46px;
    background: var(--bronze); color: var(--menu-text);
    font-size: 31px; letter-spacing: 11px; text-align: center; line-height: 46px;
    padding-left: 8px;
  }

  .section-title { position: absolute; left: 30px; top: 26px; font-size: 18px; letter-spacing: 5.5px; color: var(--ink); }
  .dish { position: absolute; left: 30px; width: 320px; }
  .dish-name { font-size: 13px; letter-spacing: 4px; color: var(--bronze); line-height: 18px; }
  .dish-desc { font-size: 13px; letter-spacing: 0.9px; color: var(--body-text); line-height: 18px; }
</style>
</head>
<body>

<section class="card card--cover" aria-label="Menu cover">
  <svg class="cover-art" viewBox="0 0 441 880" role="img" aria-label="Stepped block of bronze squares rising along the right edge">
    <defs>
      <linearGradient id="coverFill" x1="0" y1="0" x2="0" y2="1">
        <stop offset="0" stop-color="var(--bronze-light)"/>
        <stop offset="1" stop-color="var(--bronze)"/>
      </linearGradient>
    </defs>
    <polygon fill="url(#coverFill)" points="362,29 406,29 406,847 185,847 185,674 244,674 244,480 303,480 303,224 362,224"/>
  </svg>

  <div class="brand brand--cover">QUAY MERIDIAN<span class="brand-sub">CAFÉ</span></div>
  <div class="menu-label">MENU</div>
</section>

<section class="card card--breakfast" aria-label="Breakfast menu">
  <h1 class="section-title">THE BREAKFAST</h1>

  <div class="dish" style="top:63px">
    <h2 class="dish-name">BUTTER CROISSANT</h2>
    <p class="dish-desc">Served plain with a selection of two jams, a<br>vanilla custard cream, a chocolate Cream<br>and butter curls).</p>
  </div>
  <div class="dish" style="top:151px">
    <h2 class="dish-name">CHEESE CROISSANT</h2>
    <p class="dish-desc">Crumbly freshly baked with cheese filling.</p>
  </div>
  <div class="dish" style="top:205px">
    <h2 class="dish-name">DAILY FRESH EGGS</h2>
    <p class="dish-desc">A choice of poached, scrambled, pan fried,<br>omelet) all served with toasted bread,<br>mushrooms, roasted tomatoes and chicken<br>sausages.</p>
  </div>
  <div class="dish" style="top:311px">
    <h2 class="dish-name">HEALTHY TIME</h2>
    <p class="dish-desc">One choice of hot beverage from our cafe<br>served with fruit salad, natural<br>Yoghurt, whole wheat bread vegetable<br>sandwiches and sugar free biscuits<br>selection.</p>
  </div>
  <div class="dish" style="top:435px">
    <h2 class="dish-name">ENERGY TIME</h2>
    <p class="dish-desc">One choice of hot beverage from our cafe<br>served with finger chocolate muffins,<br>Poached egg with toasted bread and crispy<br>beef bacon, crepe roll with goat<br>Cheese and honey and finger chocolate<br>cream with salted cookies.</p>
  </div>
  <div class="dish" style="top:577px">
    <h2 class="dish-name">QUAY MERIDIAN TIME</h2>
    <p class="dish-desc">One choice of hot beverage from our cafe<br>served with our selection of scones, Smoked<br>salmon and avocado sandwich, roasted<br>sausages sandwich, grilled vegetables<br>sandwich, selection of our best biscuits.</p>
  </div>
  <div class="dish" style="top:701px">
    <h2 class="dish-name">THE ARABIC BREAKFAST</h2>
    <p class="dish-desc">Choice of Zattar Manakish and Cheese<br>Manakish, served with one choice of hot<br>beverage from our cafe and fresh orange<br>juice.</p>
  </div>

  <div class="brand brand--small">QUAY MERIDIAN CAFÉ</div>

  <svg class="side-art" viewBox="0 0 45 820" role="img" aria-label="Column of pale sand and grey squares">
    <defs>
      <linearGradient id="sideFill" x1="0" y1="0" x2="0" y2="1">
        <stop offset="0" stop-color="var(--sand)"/>
        <stop offset="1" stop-color="var(--stone)"/>
      </linearGradient>
    </defs>
    <rect width="45" height="820" fill="url(#sideFill)"/>
  </svg>
</section>

</body>
</html>
```